Health Coaching Brochure for Healthcare Practioners

I am looking to have a tri-fold brochure created marketed towards healthcare practitioners (doctors, nurses, surgeons, etc), to get them to purchase 1-on-1 health coaching from me.
I've provided the text/content (in pdf & pages), my logo, a picture of me, and two color palettes, but please also include lots of white space. I would like to design to be very clean, modern & crisp. Also include additional photos, of doctors, etc taking care of themselves & feeling happy (maybe eating healthy, maybe exercising, feeling good & happy!)
Please also see http://tallbirchwellness.com and http://instagram.com/tallbirchwellness for a feel of my brand.
Thank you!
Target Market(s)
Healthcare Practioners (mainly based in Los Angeles, for now)
Industry/Entity Type
Healthcare
Look and feel
Each slider illustrates characteristics of the customer's brand and the style your logo design should communicate.

```html
<!DOCTYPE html>
<html lang="en">
<head>
<meta charset="utf-8">
<title>Tall Birch Wellness – Health Coaching Tri-fold Brochure</title>
<link href="https://fonts.googleapis.com/css2?family=Mulish:ital,wght@0,400;0,600;0,800;1,400&family=Dancing+Script:wght@400&family=Caveat:wght@400&display=swap" rel="stylesheet">
<style>
  :root {
    --teal: #14a9a7;
    --slate: #363944;
    --slate-deep: #2b2e37;
    --ink: #2a2c33;
    --grey: #7d8088;
    --story: #d9dbe0;
    --white: #ffffff;
    --page: #ffffff;
  }
  * { margin: 0; padding: 0; box-sizing: border-box; }
  html, body { width: 923px; height: 1200px; overflow: hidden; background: var(--page); }
  body { position: relative; font-family: "Mulish", sans-serif; color: var(--ink); }

  .side-label {
    position: absolute; left: 79px;
    font-family: "Caveat", cursive; font-size: 38px; color: #111;
    white-space: nowrap; transform: translate(-50%, -50%) rotate(-90deg);
  }
  .side-label--a { top: 427px; }
  .side-label--b { top: 1000px; }

  .sheet {
    position: absolute; left: 103px; width: 786px; height: 561px;
    overflow: hidden; box-shadow: 1px 2px 3px rgba(0,0,0,.25);
  }
  .sheet--outer { top: 27px; }
  .sheet--inner { top: 600px; }
  .sheet__art { position: absolute; inset: 0; width: 786px; height: 561px; }

  .abs { position: absolute; }
  .heading { font-weight: 800; font-size: 15px; color: var(--white); white-space: nowrap; }
  .heading--dark { color: var(--ink); }

  /* Outer cover */
  .intro { left: 32px; top: 333px; width: 210px; font-size: 7.6px; line-height: 1.45; color: var(--white); text-align: justify; }
  .goals { left: 34px; top: 384px; list-style: none; }
  .goals li { position: relative; padding-left: 17px; height: 33.5px; font-size: 12.5px; color: var(--white); white-space: nowrap; }
  .goals li::before {
    content: ""; position: absolute; left: 0; top: 4px; width: 6px; height: 6px;
    border: 1.2px solid var(--white); border-radius: 50%;
  }
  .location-note { left: 264px; width: 257px; top: 412px; text-align: center; font-size: 6.8px; color: var(--white); }
  .consult-call { left: 264px; width: 257px; top: 422px; text-align: center; font-family: "Dancing Script", cursive; font-size: 14px; color: var(--white); }
  .contact-list { left: 290px; top: 476px; list-style: none; font-size: 6.8px; color: var(--white); line-height: 13.3px; }
  .social { left: 290px; top: 517px; display: flex; align-items: center; gap: 5px; font-size: 7px; color: var(--white); }
  .social__dot { width: 9px; height: 9px; border: 1.2px solid var(--white); border-radius: 2px; }
  .brand { left: 524px; width: 262px; top: 38px; text-align: center; font-weight: 800; font-size: 22px; color: var(--ink); letter-spacing: .3px; }
  .cover-title { left: 524px; width: 262px; top: 172px; text-align: center; font-weight: 400; font-size: 20px; line-height: 1.3; color: var(--white); }

  /* Inner page */
  .perks { left: 33px; top: 76px; list-style: none; }
  .perks li { position: relative; padding-left: 13px; font-size: 8.4px; line-height: 13.7px; color: var(--grey); white-space: nowrap; }
  .perks li::before {
    content: ""; position: absolute; left: 1px; top: 3px; width: 3.5px; height: 6px;
    border: solid var(--teal); border-width: 0 2px 2px 0; transform: rotate(40deg);
  }
  .access { left: 32px; top: 364px; width: 215px; font-weight: 800; font-size: 17px; line-height: 21px; color: var(--teal); }
  .coaching { left: 32px; top: 424px; width: 190px; font-weight: 800; font-size: 15.5px; line-height: 20px; color: var(--teal); }
  .benefit { left: 303px; display: flex; align-items: center; gap: 12px; font-size: 6.8px; line-height: 1.6; color: var(--white); }
  .benefit__check {
    position: relative; flex: none; width: 26px; height: 26px; border: 1.5px solid var(--white); border-radius: 50%;
  }
  .benefit__check::after {
    content: ""; position: absolute; left: 9px; top: 6px; width: 5px; height: 9px;
    border: solid var(--white); border-width: 0 1.8px 1.8px 0; transform: rotate(40deg);
  }
  .story { left: 290px; width: 208px; font-size: 7px; line-height: 11.2px; color: var(--story); text-align: justify; }
  .quote { left: 546px; width: 210px; font-style: italic; font-size: 6.4px; line-height: 11px; color: var(--grey); }
  .signature { left: 546px; width: 210px; text-align: right; font-family: "Dancing Script", cursive; font-size: 10px; line-height: 12px; color: var(--grey); }
</style>
</head>
<body>

<div class="side-label side-label--a">Outer Cover - Side A</div>
<div class="side-label side-label--b">Internal Page - Side B</div>

<!-- OUTER COVER -->
<section class="sheet sheet--outer">
  <svg class="sheet__art" viewBox="0 0 786 561">
    <defs>
      <linearGradient id="gradStretch" x1="0" y1="0" x2="1" y2="1">
        <stop offset="0" stop-color="#8c8f8e"/><stop offset=".5" stop-color="#c9a98e"/><stop offset="1" stop-color="#4a4a48"/>
      </linearGradient>
      <linearGradient id="gradPortrait" x1="0" y1="0" x2="0" y2="1">
        <stop offset="0" stop-color="#bdb5aa"/><stop offset=".5" stop-color="#c79a82"/><stop offset="1" stop-color="#e8e3dd"/>
      </linearGradient>
      <linearGradient id="gradShore" x1="0" y1="0" x2="0" y2="1">
        <stop offset="0" stop-color="#5e8592"/><stop offset=".5" stop-color="#4f564e"/><stop offset="1" stop-color="#3d3a33"/>
      </linearGradient>
      <linearGradient id="gradMap" x1="0" y1="0" x2="1" y2="1">
        <stop offset="0" stop-color="#e6e2d3"/><stop offset="1" stop-color="#cfdcc2"/>
      </linearGradient>
    </defs>
    <g role="img" aria-label="Photo of a practitioner stretching outdoors at sunset">
      <rect x="0" y="0" width="264" height="320" fill="url(#gradStretch)"/>
    </g>
    <polygon points="0,218 264,306 264,545 0,545" fill="var(--teal)"/>
    <rect x="0" y="545" width="264" height="16" fill="var(--slate-deep)"/>
    <g role="img" aria-label="Portrait photo of the health coach">
      <rect x="264" y="0" width="257" height="310" fill="url(#gradPortrait)"/>
    </g>
    <polygon points="264,306 521,220 521,545 264,545" fill="var(--slate)"/>
    <rect x="264" y="545" width="257" height="16" fill="var(--teal)"/>
    <g role="img" aria-label="Map of the Los Angeles area">
      <rect x="320" y="336" width="144" height="71" fill="url(#gradMap)" stroke="var(--teal)" stroke-width="2"/>
    </g>
    <rect x="521" y="0" width="265" height="561" fill="var(--white)"/>
    <g role="img" aria-label="Photo of a woman holding a calm yoga stance on coastal rocks">
      <polygon points="521,280 786,330 786,561 521,561" fill="url(#gradShore)"/>
    </g>
    <polygon points="521,92 786,156 786,340 521,280" fill="var(--teal)" opacity=".96"/>
    <line x1="32" y1="323" x2="52" y2="323" stroke="var(--white)" stroke-width="2"/>
    <line x1="290" y1="326" x2="310" y2="326" stroke="var(--teal)" stroke-width="2"/>
  </svg>

  <h2 class="abs heading" style="left:32px;top:301px;">Take care of you, too</h2>
  <p class="abs intro">You care for patients all day. Who cares for you? Schedule your complimentary 15-minute consultation to discuss your shifts, stress and goals.</p>
  <ul class="abs goals">
    <li>MORE ENERGY</li>
    <li>BETTER SLEEP</li>
    <li>LESS STRESS</li>
    <li>LOOK &amp; FEEL BETTER THAN EVER</li>
  </ul>

  <h2 class="abs heading" style="left:290px;top:304px;">About Me</h2>
  <p class="abs location-note">Glendale office or virtual sessions</p>
  <p class="abs consult-call">Call for a free 15 minute consultation</p>
  <h2 class="abs heading" style="left:290px;top:449px;">Contact</h2>
  <ul class="abs contact-list">
    <li>555.010.4821</li>
    <li>maren@tallbirchwellness.com</li>
    <li>www.tallbirchwellness.com</li>
  </ul>
  <div class="abs social"><span class="social__dot"></span>@tallbirchwellness</div>

  <div class="abs brand">tall birch wellness</div>
  <h1 class="abs cover-title">1-on-1 Health Coaching,<br>Los Angeles, CA</h1>
</section>

<!-- INTERNAL PAGE -->
<section class="sheet sheet--inner">
  <svg class="sheet__art" viewBox="0 0 786 561">
    <defs>
      <linearGradient id="gradRunner" x1="0" y1="0" x2="1" y2="1">
        <stop offset="0" stop-color="#e9b86b"/><stop offset=".5" stop-color="#d8a484"/><stop offset="1" stop-color="#7a6a5c"/>
      </linearGradient>
      <linearGradient id="gradPath" x1="0" y1="0" x2="0" y2="1">
        <stop offset="0" stop-color="#3f5a35"/><stop offset=".5" stop-color="#4b5143"/><stop offset="1" stop-color="#6b5e52"/>
      </linearGradient>
    </defs>
    <rect x="0" y="0" width="264" height="561" fill="var(--white)"/>
    <rect x="0" y="0" width="238" height="14" fill="var(--teal)"/>
    <g role="img" aria-label="Photo of a smiling practitioner out for a sunny run with earphones">
      <polygon points="0,307 264,219 264,545 0,545" fill="url(#gradRunner)"/>
    </g>
    <rect x="0" y="545" width="264" height="16" fill="var(--slate-deep)"/>
    <rect x="264" y="0" width="257" height="561" fill="var(--slate)"/>
    <polygon points="264,0 521,0 521,304 264,219" fill="var(--teal)"/>
    <rect x="521" y="0" width="265" height="561" fill="var(--white)"/>
    <g role="img" aria-label="Photo of a woman power walking along a garden path">
      <polygon points="521,0 786,0 786,216 521,304" fill="url(#gradPath)"/>
    </g>
    <rect x="547" y="545" width="239" height="16" fill="var(--slate-deep)"/>
    <line x1="32" y1="414" x2="52" y2="414" stroke="var(--teal)" stroke-width="2"/>
    <line x1="290" y1="57" x2="310" y2="57" stroke="var(--white)" stroke-width="2"/>
    <line x1="290" y1="327" x2="310" y2="327" stroke="var(--teal)" stroke-width="2"/>
    <line x1="546" y1="357" x2="566" y2="357" stroke="var(--teal)" stroke-width="2"/>
  </svg>

  <h2 class="abs heading heading--dark" style="left:33px;top:33px;width:210px;font-size:13.5px;line-height:1.15;white-space:normal;">Get more out of your day with a health coach.</h2>
  <ul class="abs perks">
    <li>Customized wellness plan that fits long and<br>irregular shifts.</li>
    <li>Provide motivation, support, and accountability</li>
    <li>Reach your health goals and enjoy the process.</li>
    <li>Stress Management.</li>
    <li>Sleep &amp; Recovery.</li>
    <li>Energy for Long Shifts.</li>
    <li>Healthy Eating on the Go.</li>
    <li>Meal Planning &amp; Prep.</li>
    <li>Movement That Fits Your Day.</li>
    <li>Nutrition &amp; Supplementation Counselling.</li>
    <li>Burnout Prevention.</li>
    <li>Work-Life Balance.</li>
  </ul>
  <p class="abs access">+24-HOUR ACCESS TO YOUR COACH</p>
  <p class="abs coaching">Integrative Nutrition &amp; Health Coaching for practitioners.</p>

  <h2 class="abs heading" style="left:290px;top:33px;">Benefits for you.</h2>
  <div class="abs benefit" style="top:70px;"><span class="benefit__check"></span><p>Coaching built around your shifts!<br>Plans that fit nights, on-call and long days.</p></div>
  <div class="abs benefit" style="top:114px;"><span class="benefit__check"></span><p>Ready to make the commitment?<br>Schedule your 15 minute consultation today!</p></div>

  <h2 class="abs heading" style="left:290px;top:300px;">Let's do it together!</h2>
  <p class="abs story" style="top:336px;">You spend your days caring for others. Health coaching gives that care back to you. I help doctors, nurses and surgeons build habits that last. My clients become more energized, more rested, calmer and stronger in all aspects of their life.</p>
  <p class="abs story" style="top:386px;">Working with practitioners at every career stage, I fit coaching around your schedule and teach you how to live a healthier life.</p>

  <h2 class="abs heading heading--dark" style="left:546px;top:331px;">Testimonials</h2>
  <p class="abs quote" style="top:364px;">"Maren is a great coach! Working nights in the ER, I lived on coffee and vending snacks. She's part coach, part nutritionist and part life-coach. She's tough as well as supportive. She helped me build habits that fit my shifts. I recommend Maren to every nurse I know."</p>
  <p class="abs signature" style="top:422px;">Dana Whitfield, RN</p>
  <p class="abs quote" style="top:438px;">"Maren is an incredible coach! She's encouraging, thoughtful, and knowledgeable about nutrition + stress. She breaks things down in an accessible way, from quick meals to recovery after long cases. She's passionate about what she does and it's contagious. I sleep better and my relationship with food has shifted. I recommend her strongly!"</p>
  <p class="abs signature" style="top:507px;">Tess Marlow, MD</p>
</section>

</body>
</html>
```